Staff Newsletter Template Image

We are looking for two .jpg images that we can put into a Word document and use for our staff newsletter. We will then add content using text boxes.
Attached is the current template which works for the columns and size that we need but we just want a fresh new design.
The Word document shows how we use it.
The name will stay the same - Team upBeat but can be a different look to the current one.

Target Market(s)

Sales team

Colors

Designer to choose colors to be used in the design.

Requirements
Must have
• Colours will be green, grey and white, possibly cream if needed. All from the guidelines.
• I have attached our brand guidelines which shows design elements and fonts for our brand. Also attached is brand guidelines for one of our product lines as we would like to use the same green.
• It needs to be nice to look at and motivational for our team

```html
<!DOCTYPE html>
<html lang="en">
<head>
<meta charset="utf-8">
<title>Weekly Team Newsletter</title>
<link rel="stylesheet" href="https://fonts.googleapis.com/css2?family=Jost:wght@300;400;600&display=swap">
<style>
  :root{
    --green:#8dc63f;
    --charcoal:#3a3a3c;
    --white:#ffffff;
  }
  *{margin:0;padding:0;box-sizing:border-box;}
  html,body{width:849px;height:1200px;overflow:hidden;background:var(--white);}
  body{font-family:"Jost",sans-serif;color:var(--charcoal);}
  .newsletter{position:relative;width:849px;height:1200px;overflow:hidden;}
  .header-shapes{position:absolute;left:0;top:0;}
  .brand-name{position:absolute;left:62px;top:48px;font-size:44px;font-weight:600;color:var(--white);letter-spacing:.5px;line-height:1;}
  .issue-date{position:absolute;left:583px;top:114px;font-size:16px;font-weight:600;color:var(--white);}
  .greeting{position:absolute;left:62px;top:210px;font-size:16px;font-weight:600;color:var(--charcoal);}
  .sidebar{position:absolute;left:424px;top:167px;width:425px;height:968px;background:var(--charcoal);color:var(--white);text-align:center;}
  .sidebar-title{position:absolute;left:0;right:0;top:42px;font-size:17px;font-weight:600;}
  .sidebar-intro{position:absolute;left:0;right:0;top:78px;font-size:15px;font-weight:300;line-height:21px;}
  .sales-basis{position:absolute;left:0;right:0;top:145px;font-size:14px;font-weight:600;}
  .rule{position:absolute;left:124px;width:173px;height:2px;background:var(--white);}
  .rule-basis{top:168px;}
  .rule-tip{top:383px;}
  .rule-shout{top:736px;}
  .leaderboard{position:absolute;left:29px;top:196px;width:365px;border:3px solid var(--white);border-collapse:separate;border-spacing:3px;background:var(--white);}
  .leaderboard td{background:var(--charcoal);height:34px;font-size:14px;font-weight:300;text-align:left;padding-left:16px;letter-spacing:.3px;}
  .leaderboard td.rank{width:45px;padding-left:0;text-align:center;font-weight:600;}
  .leaderboard tr:first-child td.rank{font-weight:300;}
  .tip-title{position:absolute;left:0;right:0;top:392px;font-size:14px;font-weight:600;}
  .tip-body{position:absolute;left:0;right:0;top:419px;font-size:15px;font-weight:300;}
  .shout-title{position:absolute;left:0;right:0;top:745px;font-size:14px;font-weight:600;}
  .shout-name{position:absolute;left:0;right:0;top:778px;font-size:14px;font-weight:600;}
  .shout-name .star{font-size:9px;vertical-align:1px;}
  .shout-comments{position:absolute;left:0;right:0;top:809px;font-size:14px;font-weight:300;letter-spacing:.3px;}
  .footer-band{position:absolute;left:0;top:1154px;width:797px;height:9px;background:var(--green);border-radius:0 9px 0 0;}
  .footer{position:absolute;left:0;top:1168px;width:849px;height:32px;background:var(--charcoal);color:var(--white);font-size:14px;font-weight:300;padding:10px 0 0 62px;}
</style>
</head>
<body>
<div class="newsletter">
  <svg class="header-shapes" width="849" height="160" viewBox="0 0 849 160" aria-hidden="true">
    <path d="M0 0H849V72H591C520 72 480 90 430 118C395 138 375 154 340 154H0Z" fill="var(--green)"/>
    <path d="M591 85H849V154H424L492 115C530 96 560 85 591 85Z" fill="var(--charcoal)"/>
  </svg>
  <div class="brand-name">Brightwell</div>
  <div class="issue-date">Date</div>

  <p class="greeting">Hi Everyone,</p>

  <aside class="sidebar">
    <h2 class="sidebar-title">TOP SELLERS!</h2>
    <p class="sidebar-intro">THE FOLLOWING CORELINK TEAM MEMBERS<br>WERE OUR TOP SELLERS LAST WEEK</p>
    <p class="sales-basis">BASED ON COMPLETED SALES</p>
    <div class="rule rule-basis"></div>
    <table class="leaderboard">
      <tr><td class="rank">#</td><td>TEAM MEMBER</td></tr>
      <tr><td class="rank">1</td><td>- 100 CORELINK DOLLARS</td></tr>
      <tr><td class="rank">2</td><td>- 50 CORELINK DOLLARS</td></tr>
      <tr><td class="rank">3</td><td>- 25 CORELINK DOLLARS</td></tr>
    </table>
    <div class="rule rule-tip"></div>
    <h3 class="tip-title">TOP TIP FROM OUR WEEK’S TOP SELLER</h3>
    <p class="tip-body">[TIP]</p>
    <div class="rule rule-shout"></div>
    <h3 class="shout-title">SHOUT OUT</h3>
    <p class="shout-name"><span class="star">★</span> NAME <span class="star">★</span></p>
    <p class="shout-comments">COMMENTS</p>
  </aside>

  <div class="footer-band"></div>
  <footer class="footer">© CORELINK RECLINERS</footer>
</div>
</body>
</html>
```